NEW Wordpress Website Design for a Dynamic Long Term Healthcare Company in Hawaii

I would like a new website design for my current company, Marlow Haven Partners, which has two different brands - Marlow Homecare and Marlow Senior Living. You can see the current website at www.marlowhaven.example. The website should be built using Wordpress Software and the Elementor theme. The website should have a local Hawaii island/tropical feel, but look professional for healthcare. I'm looking for something fresh, and want the designer to select colors, styles, etc.

In the Header, on all pages, I would like a menu that includes Home Care, Senior Living, Rates, and About Us.
Under each of the Header Menu Titles, I would like these drop downs included:
Home Care (drop down pages)- Nurse Aide Care, 24-Hour Home Care, Skilled Nursing, Lifestyle Aide, Hospice at Home, Bathing & Meal Service.
Senior Living (drop down pages) - Long-Term Stay, Short-Term Stay.
Rates (drop down page) - Rates.
About Us (drop down pages) - Our Mission, Ohana Talk, About Doreen Marlow.

In the footer, on all pages, you should include the address: 248 Lanakila Ave, Suite 310, Honolulu, HI 96817. Phone number: 808-555-0173
The footer should also include buttons for a page called Learn, Caregiver Jobs, and each of the service page links to include: Nurse Aide Care, 24-Hour Home Care, Skilled Nursing, Lifestyle Aide, Hospice at Home, Bathing & Meal Service.
Please don't take the current website and redesign a few aspects. I'm looking for a completely different look and feel.

Target Market(s)

40-80 year olds

Industry/Entity Type

Long Term Healthcare

Coding

Coded - Design and coding required

Requirements
Should not have
• Our existing website as a template. We are looking for a complete redesign. Thank you.

```html
<!DOCTYPE html>
<html lang="en">
<head>
<meta charset="utf-8">
<title>Marlow Haven Partners – Homecare &amp; Senior Living</title>
<link rel="stylesheet" href="https://fonts.googleapis.com/css2?family=Roboto:wght@300;400;500;700&family=Libre+Baskerville&display=swap">
<style>
:root{
  --coral:#f3a38f;
  --teal:#86bdc4;
  --teal-arch:#94cbd0;
  --teal-soft:#a9cfd3;
  --ink:#2e2e30;
  --text:#4a4a4a;
  --field:#ececec;
  --footer-box:#4a4a4c;
  --white:#ffffff;
}
*{box-sizing:border-box;margin:0;padding:0}
html,body{width:1200px;height:3647px;overflow:hidden}
body{position:relative;background:var(--white);font-family:'Roboto',sans-serif;color:var(--text)}
.abs{position:absolute}

.site-header{position:absolute;left:0;top:0;width:1200px;height:88px;background:var(--white);z-index:5}
.brand{position:absolute;left:89px;top:14px;display:flex;align-items:center;gap:10px}
.brand-mark{width:56px;height:56px;border-radius:8px;background:var(--ink)}
.brand-name{font-weight:400;font-size:26px;color:var(--ink);line-height:1}
.contact-item{position:absolute;top:18px;display:flex;gap:14px;align-items:flex-start}
.contact-item small{display:block;font-size:12px;color:var(--ink);letter-spacing:.2px}
.contact-item strong{display:block;font-size:16px;font-weight:500;color:var(--ink);margin-top:3px}
.main-nav{position:absolute;left:613px;top:66px;width:587px;height:54px;background:var(--teal);border-radius:8px 0 0 8px;display:flex;align-items:center;padding-left:67px;z-index:6}
.main-nav a{color:var(--white);font-size:12px;font-weight:500;text-decoration:none;margin-right:30px;display:flex;align-items:center;gap:6px}
.main-nav svg{width:8px;height:6px}

.hero{position:absolute;left:0;top:88px;width:1200px;height:760px}
.hero-kicker{position:absolute;left:88px;top:190px;font-family:'Libre Baskerville',serif;font-size:38px;color:var(--white)}
.hero-title{position:absolute;left:88px;top:234px;color:var(--white);font-size:64px;line-height:70px;font-weight:400}
.hero-title b{font-weight:700}
.btn{position:absolute;display:flex;align-items:center;gap:12px;color:var(--white);font-size:12px;font-weight:700;text-transform:uppercase;text-decoration:none;padding-left:10px;border-radius:5px}
.btn .btn-icon{width:30px;height:26px;border:2px solid var(--white);border-radius:6px}
.btn-coral{background:var(--coral)}
.btn-teal{background:var(--teal-soft)}

.brand-card{position:absolute;top:893px;width:460px;height:287px;border-radius:14px;overflow:hidden}
.card-badge{position:absolute;width:128px;height:128px;border-radius:50%;background:var(--white);display:flex;align-items:center;justify-content:center;text-align:center;font-size:15px;line-height:18px;color:#3c8d92;box-shadow:0 4px 10px rgba(0,0,0,.08)}
.card-caption{position:absolute;top:1244px;width:460px;text-align:center;font-size:12.5px;line-height:19px;color:var(--text)}

.band-bg{position:absolute;left:0;top:1323px;width:1200px;height:998px}
.section-title{position:absolute;font-size:40px;line-height:44px;font-weight:300;color:var(--ink)}
.section-title b{font-weight:700}
.section-copy{position:absolute;font-size:12.5px;line-height:18.5px;color:var(--text)}
.photo{position:absolute;overflow:hidden}
.photo-circle{position:absolute;border-radius:50%;border:6px solid var(--white);box-shadow:0 6px 16px rgba(0,0,0,.15)}

.consult-card{position:absolute;left:457px;top:2410px;width:654px;height:463px;background:var(--white);border-radius:22px;box-shadow:0 8px 30px rgba(0,0,0,.07)}
.field{position:absolute;height:47px;background:var(--field);border-radius:3px;font-size:13px;color:#555;display:flex;align-items:center;justify-content:space-between;padding:0 18px}
.field svg{width:10px;height:7px}
.consent{position:absolute;left:637px;top:2738px;font-size:11.5px;line-height:16px;color:var(--ink)}

.quote{position:absolute;left:0;top:2995px;width:1200px;text-align:center;font-size:27px;line-height:38px;color:var(--ink);font-weight:300}

.footer-bg{position:absolute;left:0;top:3113px;width:1200px;height:534px}
.footer-brand{position:absolute;left:119px;top:3390px;display:flex;align-items:center;gap:12px;color:var(--white);font-size:40px;font-weight:400}
.footer-brand span.dot{width:30px;height:30px;border-radius:50%;border:2px solid var(--white)}
.footer-heading{position:absolute;top:3324px;color:var(--white);font-size:18px;font-weight:700}
.footer-list{position:absolute;left:350px;top:3361px;list-style:none}
.footer-list li{font-size:12.5px;color:#e2e2e2;line-height:24.8px}
.contact-row{position:absolute;left:577px;display:flex;gap:20px}
.contact-row svg{width:20px;height:22px;margin-top:4px}
.contact-row b{display:block;color:var(--white);font-size:12px;font-weight:700}
.contact-row span{display:block;color:#e2e2e2;font-size:12.5px;line-height:19px}
.footer-rule{position:absolute;left:573px;top:3444px;width:265px;height:1px;background:#565658}
.footer-box{position:absolute;left:876px;top:3340px;width:235px;height:176px;background:var(--footer-box);border-radius:12px}
.footer-btn{position:absolute;left:901px;width:186px;height:43px;border-radius:3px;display:flex;align-items:center;justify-content:center;color:var(--white);font-size:14px;font-weight:700;text-transform:uppercase}
.bottom-rule{position:absolute;left:89px;top:3599px;width:1022px;height:1px;background:#5a5a5c}
.copyright{position:absolute;left:89px;top:3614px;font-size:12px;color:#d6d6d6}
.social{position:absolute;top:3614px;width:14px;height:14px;border-radius:50%;background:#e8e8e8}
.to-top{position:absolute;left:1120px;top:3578px;width:38px;height:38px;border-radius:50%;background:var(--teal-soft);display:flex;align-items:center;justify-content:center}

/* photo tone fills */
.tone-homecare{background:
  radial-gradient(circle at 72% 55%,rgba(70,160,215,.95) 0,rgba(70,160,215,0) 32%),
  radial-gradient(circle at 40% 45%,rgba(205,180,160,.9) 0,rgba(205,180,160,0) 28%),
  radial-gradient(circle at 15% 85%,rgba(120,80,50,.9) 0,rgba(120,80,50,0) 35%),
  linear-gradient(135deg,#e6dc9e 0%,#c9c18a 40%,#b8b28f 70%,#a89a78 100%)}
.tone-senior{background:
  radial-gradient(ellipse at 50% 8%,rgba(110,70,40,1) 0,rgba(110,70,40,0) 40%),
  radial-gradient(circle at 53% 60%,rgba(215,60,60,.9) 0,rgba(215,60,60,0) 16%),
  radial-gradient(circle at 70% 50%,rgba(70,140,210,.9) 0,rgba(70,140,210,0) 18%),
  radial-gradient(circle at 15% 35%,rgba(190,225,140,.9) 0,rgba(190,225,140,0) 22%),
  radial-gradient(circle at 88% 35%,rgba(160,210,120,.9) 0,rgba(160,210,120,0) 22%),
  linear-gradient(180deg,#e9d9a8 0%,#c6ad7c 60%,#8c6d48 100%)}
.tone-nurse{background:
  radial-gradient(circle at 50% 30%,rgba(200,150,120,.95) 0,rgba(200,150,120,0) 22%),
  radial-gradient(circle at 45% 18%,rgba(40,30,30,.9) 0,rgba(40,30,30,0) 20%),
  radial-gradient(ellipse at 35% 70%,rgba(40,150,170,.95) 0,rgba(40,150,170,0) 40%),
  radial-gradient(circle at 80% 55%,rgba(255,255,255,1) 0,rgba(255,255,255,0) 45%),
  linear-gradient(120deg,#dfe6e8 0%,#c9d6d8 40%,#eef1f2 100%)}
.tone-lounge{background:
  radial-gradient(circle at 35% 55%,rgba(160,60,130,.9) 0,rgba(160,60,130,0) 25%),
  radial-gradient(circle at 65% 60%,rgba(200,110,80,.9) 0,rgba(200,110,80,0) 25%),
  radial-gradient(circle at 50% 15%,rgba(240,240,230,1) 0,rgba(240,240,230,0) 40%),
  linear-gradient(180deg,#d8d2bb 0%,#a88e6e 100%)}
.tone-dining{background:
  radial-gradient(circle at 55% 45%,rgba(170,30,50,.95) 0,rgba(170,30,50,0) 25%),
  radial-gradient(circle at 30% 65%,rgba(230,225,225,.9) 0,rgba(230,225,225,0) 22%),
  radial-gradient(ellipse at 50% 90%,rgba(90,50,30,1) 0,rgba(90,50,30,0) 45%),
  linear-gradient(180deg,#d8c9ab 0%,#a88a6a 100%)}
.tone-room{background:
  radial-gradient(ellipse at 50% 75%,rgba(70,40,25,1) 0,rgba(70,40,25,0) 40%),
  radial-gradient(circle at 65% 25%,rgba(255,250,235,1) 0,rgba(255,250,235,0) 35%),
  linear-gradient(180deg,#f0e6d0 0%,#d7c19b 55%,#8a6a48 100%)}
.tone-consult{background:
  radial-gradient(circle at 18% 45%,rgba(60,35,25,1) 0,rgba(60,35,25,0) 30%),
  radial-gradient(circle at 30% 35%,rgba(170,115,85,.95) 0,rgba(170,115,85,0) 18%),
  radial-gradient(ellipse at 45% 70%,rgba(110,195,190,.95) 0,rgba(110,195,190,0) 35%),
  radial-gradient(circle at 78% 50%,rgba(235,210,200,1) 0,rgba(235,210,200,0) 22%),
  linear-gradient(100deg,#7a5a48 0%,#c8b0a0 45%,#f0eeec 100%)}
</style>
</head>
<body>

<header class="site-header">
  <div class="brand">
    <span class="brand-mark"></span>
    <span class="brand-name">Marlow Haven</span>
  </div>
  <div class="contact-item" style="left:719px">
    <svg width="18" height="30" viewBox="0 0 18 30"><rect x="1.5" y="1.5" width="15" height="27" rx="3" fill="none" stroke="#f3a38f" stroke-width="2"/><line x1="6" y1="24" x2="12" y2="24" stroke="#f3a38f" stroke-width="2"/></svg>
    <div><small>CALL US NOW:</small><strong>808-555-0173</strong></div>
  </div>
  <div class="contact-item" style="left:934px">
    <svg width="30" height="30" viewBox="0 0 30 30"><circle cx="15" cy="15" r="13" fill="none" stroke="#f3a38f" stroke-width="2"/><path d="M15 7v8l-5 4" fill="none" stroke="#f3a38f" stroke-width="2"/></svg>
    <div><small>OFFICE HOURS:</small><strong>8:30AM - 5:30PM</strong></div>
  </div>
</header>

<nav class="main-nav">
  <a href="#">HOME CARE <svg viewBox="0 0 8 6"><path d="M1 1l3 3 3-3" fill="none" stroke="#fff" stroke-width="1.2"/></svg></a>
  <a href="#">SENIOR LIVING <svg viewBox="0 0 8 6"><path d="M1 1l3 3 3-3" fill="none" stroke="#fff" stroke-width="1.2"/></svg></a>
  <a href="#">RATES <svg viewBox="0 0 8 6"><path d="M1 1l3 3 3-3" fill="none" stroke="#fff" stroke-width="1.2"/></svg></a>
  <a href="#">ABOUT US <svg viewBox="0 0 8 6"><path d="M1 1l3 3 3-3" fill="none" stroke="#fff" stroke-width="1.2"/></svg></a>
</nav>

<section class="hero">
  <svg width="1200" height="760" viewBox="0 0 1200 760">
    <defs>
      <linearGradient id="heroBase" x1="0" y1="0" x2="1" y2="1">
        <stop offset="0" stop-color="#5e5446"/>
        <stop offset=".35" stop-color="#8a7656"/>
        <stop offset=".65" stop-color="#9a8560"/>
        <stop offset="1" stop-color="#6a4a30"/>
      </linearGradient>
      <radialGradient id="heroWindow" cx=".85" cy=".1" r=".35"><stop offset="0" stop-color="#f4f0a0"/><stop offset="1" stop-color="#f4f0a0" stop-opacity="0"/></radialGradient>
      <radialGradient id="heroBlueA" cx=".6" cy=".48" r=".2"><stop offset="0" stop-color="#2f6fc4"/><stop offset="1" stop-color="#2f6fc4" stop-opacity="0"/></radialGradient>
      <radialGradient id="heroBlueB" cx=".85" cy=".5" r=".22"><stop offset="0" stop-color="#3fb0e0"/><stop offset="1" stop-color="#3fb0e0" stop-opacity="0"/></radialGradient>
      <radialGradient id="heroDenim" cx=".82" cy=".88" r=".25"><stop offset="0" stop-color="#34527a"/><stop offset="1" stop-color="#34527a" stop-opacity="0"/></radialGradient>
      <radialGradient id="heroSofa" cx=".25" cy=".8" r=".35"><stop offset="0" stop-color="#a8683a"/><stop offset="1" stop-color="#a8683a" stop-opacity="0"/></radialGradient>
      <radialGradient id="heroShade" cx=".1" cy=".35" r=".4"><stop offset="0" stop-color="#3a342c" stop-opacity=".8"/><stop offset="1" stop-color="#3a342c" stop-opacity="0"/></radialGradient>
      <clipPath id="heroClip"><path d="M0 0 H1200 V500 C1200 600 1140 640 1040 641 H170 C60 640 0 590 0 480 Z"/></clipPath>
    </defs>
    <path d="M0 470 C0 640 150 690 330 700 C480 708 560 725 600 740 C640 725 720 708 870 700 C1050 690 1200 640 1200 470 Z" fill="#ebebeb"/>
    <g role="img" aria-label="Caregiver in blue scrubs sharing a laugh with a senior woman on a living room sofa" clip-path="url(#heroClip)">
      <rect width="1200" height="660" fill="url(#heroBase)"/>
      <rect width="1200" height="660" fill="url(#heroWindow)"/>
      <rect width="1200" height="660" fill="url(#heroSofa)"/>
      <rect width="1200" height="660" fill="url(#heroBlueA)"/>
      <rect width="1200" height="660" fill="url(#heroBlueB)"/>
      <rect width="1200" height="660" fill="url(#heroDenim)"/>
      <rect width="1200" height="660" fill="url(#heroShade)"/>
    </g>
    <rect x="591" y="632" width="18" height="28" rx="9" fill="none" stroke="#fff" stroke-width="2"/>
    <line x1="600" y1="639" x2="600" y2="646" stroke="#fff" stroke-width="2"/>
  </svg>
  <div class="hero-kicker">Hawaii's Choice</div>
  <h1 class="hero-title"><b>HOMECARE</b> &amp;<br>SENIOR LIVING</h1>
  <a class="btn btn-coral" href="#" style="left:89px;top:383px;width:157px;height:41px"><span class="btn-icon"></span>Info &amp; Rates</a>
</section>

<div class="brand-card tone-homecare" role="img" aria-label="Caregiver helping a senior man with his shirt at home" style="left:132px"></div>
<div class="card-badge" style="left:298px;top:1105px">Marlow<br>Homecare</div>
<p class="card-caption" style="left:132px">Marlow Homecare provides a variety of professional in-home health care<br>services throughout the entire island of Oahu.</p>

<div class="brand-card tone-senior" role="img" aria-label="Seniors exercising with hand weights in a bright living room" style="left:607px"></div>
<div class="card-badge" style="left:773px;top:1105px">Marlow<br>Senior Living</div>
<p class="card-caption" style="left:607px">Marlow Senior Living, a beautiful Adult Residential Care Home, is<br>located on the windward side of Oahu in Kailua.</p>

<svg class="band-bg" viewBox="0 0 1200 998">
  <defs>
    <linearGradient id="bandFill" x1="0" y1="0" x2="1" y2=".3">
      <stop offset="0" stop-color="#fbe2da"/>
      <stop offset=".45" stop-color="#eef0ee"/>
      <stop offset="1" stop-color="#deedef"/>
    </linearGradient>
  </defs>
  <path d="M0 250 C0 150 80 112 210 106 C410 98 540 62 600 0 C660 62 790 98 990 106 C1120 112 1200 150 1200 250 V998 H0 Z" fill="url(#bandFill)"/>
</svg>

<div class="photo tone-nurse" role="img" aria-label="Smiling nurse with stethoscope talking on the phone" style="left:115px;top:1486px;width:488px;height:361px;border-radius:40px"></div>

<h2 class="section-title" style="left:658px;top:1558px">PROFESSIONAL<br>CARE IN <b>YOUR HOME</b></h2>
<p class="section-copy" style="left:660px;top:1655px;width:410px">Marlow Homecare understands that every person's care journey is unique. We tailor our in-home services to meet the diverse nurturing experience of professional quality care and safety within the comfort and convenience of your own home.</p>
<a class="btn btn-coral" href="#" style="left:659px;top:1748px;width:272px;height:41px"><span class="btn-icon"></span>Schedule Care Assessment</a>

<div class="abs" style="left:650px;top:1828px;width:423px;height:493px;background:var(--teal-arch);border-radius:212px 212px 0 0"></div>
<div class="photo-circle tone-lounge" role="img" aria-label="Residents sitting together on a sofa" style="left:819px;top:1907px;width:148px;height:148px"></div>
<div class="photo-circle tone-dining" role="img" aria-label="Caregiver serving a meal to seniors at a dining table" style="left:600px;top:1977px;width:206px;height:206px"></div>
<div class="photo-circle tone-room" role="img" aria-label="Bright dining room with wooden table and chairs" style="left:790px;top:2087px;width:206px;height:206px"></div>

<h2 class="section-title" style="left:117px;top:1973px">TRUSTED CARE IN<br><b>OUR HOME</b></h2>
<p class="section-copy" style="left:119px;top:2070px;width:405px">Marlow Senior Living creates a warm, supportive, and enriching care home environment where seniors can thrive in their golden years. We provide residential care that promotes well-being, connection, and dignity of each individual.</p>
<a class="btn btn-teal" href="#" style="left:119px;top:2161px;width:181px;height:42px"><span class="btn-icon"></span>Schedule Tour</a>

<div class="consult-card"></div>
<h2 class="section-title" style="left:119px;top:2459px;line-height:45px">SCHEDULE A<br><b>COMPLIMENTARY</b><br>CARE CONSULTATION</h2>
<div class="photo tone-consult" role="img" aria-label="Caregiver smiling with an elderly man" style="left:119px;top:2623px;width:478px;height:196px;border-radius:22px"></div>

<div class="field" style="left:635px;top:2462px;width:211px">Name*</div>
<div class="field" style="left:855px;top:2462px;width:211px">Email*</div>
<div class="field" style="left:635px;top:2516px;width:211px">Phone</div>
<div class="field" style="left:855px;top:2516px;width:211px">How Can We Help? <svg viewBox="0 0 10 7"><path d="M1 1l4 4 4-4" fill="none" stroke="#333" stroke-width="1.5"/></svg></div>
<div class="field" style="left:635px;top:2571px;width:429px">Questions/Comments</div>
<div class="field" style="left:635px;top:2623px;width:429px">How did you hear about us?</div>
<div class="field" style="left:635px;top:2677px;width:429px">May We Email You About This? <svg viewBox="0 0 10 7"><path d="M1 1l4 4 4-4" fill="none" stroke="#333" stroke-width="1.5"/></svg></div>
<p class="consent">You agree to receive future emails and understand<br>you may opt-out at any time</p>
<a class="btn btn-coral" href="#" style="left:634px;top:2778px;width:117px;height:42px"><span class="btn-icon"></span>Submit</a>

<svg class="abs" style="left:552px;top:2929px" width="96" height="64" viewBox="0 0 96 64">
  <path d="M4 60 C4 30 14 10 40 2 L42 10 C28 16 24 26 24 34 L42 34 L42 60 Z" fill="#a9cfd3"/>
  <path d="M52 60 C52 30 62 10 88 2 L90 10 C76 16 72 26 72 34 L90 34 L90 60 Z" fill="#a9cfd3"/>
</svg>
<p class="quote">Caregiving is a series of small acts of care that<br>alter the course of someone's life.</p>

<svg class="footer-bg" viewBox="0 0 1200 534">
  <path d="M0 150 C20 72 120 60 300 55 C460 50 560 30 600 0 C640 30 740 50 900 55 C1080 60 1180 72 1200 150 V534 H0 Z" fill="#e7e7e7"/>
  <path d="M0 205 C0 125 100 102 270 96 C450 90 560 62 600 28 C640 62 750 90 930 96 C1100 102 1200 125 1200 205 V534 H0 Z" fill="#3b3b3d"/>
</svg>

<div class="footer-brand"><span class="dot"></span>Marlow</div>

<h3 class="footer-heading" style="left:350px">MARLOW SERVICES</h3>
<ul class="footer-list">
  <li>Nurse Aide Care</li>
  <li>24-Hour Home Care</li>
  <li>Skilled Nursing</li>
  <li>Lifestyle Aide</li>
  <li>Hospice at Home</li>
  <li>Bathing &amp; Meal Service</li>
</ul>

<h3 class="footer-heading" style="left:577px">CONTACT US</h3>
<div class="contact-row" style="top:3366px">
  <svg viewBox="0 0 20 22"><path d="M10 21 C4 13 3 10 3 8 a7 7 0 0 1 14 0 c0 2 -1 5 -7 13z" fill="#86bdc4"/><circle cx="10" cy="8" r="2.5" fill="#3b3b3d"/></svg>
  <div><b>ADDRESS</b><span>248 Lanakila Ave, Suite 310,<br>Honolulu, HI 96817</span></div>
</div>
<div class="footer-rule"></div>
<div class="contact-row" style="top:3467px">
  <svg viewBox="0 0 20 22"><path d="M4 2 l4 0 l2 5 l-3 2 c1 3 3 5 6 6 l2 -3 l5 2 l0 4 c-9 1 -17 -7 -16 -16z" fill="#86bdc4"/></svg>
  <div><b>CALL NOW</b><span>808-555-0173</span></div>
</div>

<div class="footer-box"></div>
<div class="footer-btn" style="top:3399px;background:var(--coral)">Learn</div>
<div class="footer-btn" style="top:3448px;background:#5c5c5e">Caregiver Jobs</div>

<div class="bottom-rule"></div>
<p class="copyright">© 2024 Marlow Haven Partners. All Rights Reserved.</p>
<span class="social" style="left:970px"></span>
<span class="social" style="left:1011px"></span>
<span class="social" style="left:1051px"></span>
<span class="social" style="left:1091px"></span>
<div class="to-top"><svg width="10" height="7" viewBox="0 0 10 7"><path d="M1 6l4-4 4 4" fill="none" stroke="#fff" stroke-width="1.5"/></svg></div>

</body>
</html>
```